Business Createrer

Design an info-graphic which explains the process of what I do to help people and busnesses (Hotels, venues etc) divine a food and Beverage plan for success.

I have an existing website which shows the style I would like to use visit www.glenmarbury.com.au.

I have attached a PPTX showing the 4 components required and then a second page for the process and a copy of the logo and splash images.

I this works I have further design projects including promo videos for apps

Target Market(s)

Food and Beverage industry including hotels, venues, caterers and restaurants

Industry/Entity Type

Business Consultant

Font styles to use
Other font styles liked:
• sweet sans

Requirements
Must have
• icon creations and clear workflow

```html
<!DOCTYPE html>
<html lang="en">
<head>
<meta charset="utf-8">
<title>Steps of Making a New Dining Concept</title>
<link href="https://fonts.googleapis.com/css2?family=Encode+Sans+Semi+Condensed:wght@700&family=Encode+Sans:wght@300;400&display=swap" rel="stylesheet">
<style>
  :root{
    --bg:#b9dff0;
    --navy:#1f4b87;
    --accent:#18a8e6;
    --pale:#d9eef8;
    --rule:#e3f2f9;
  }
  html,body{margin:0;padding:0;overflow:hidden;background:var(--bg);}
  .canvas{position:relative;width:1200px;height:849px;overflow:hidden;background:var(--bg);color:var(--navy);font-family:"Encode Sans",sans-serif;}
  .title{position:absolute;left:38px;top:62px;margin:0;font-family:"Encode Sans Semi Condensed",sans-serif;font-weight:700;font-size:43px;letter-spacing:-0.3px;line-height:1;color:var(--navy);}
  .title-rule{position:absolute;left:38px;top:118px;width:866px;height:4px;background:var(--accent);}
  .brand{position:absolute;right:40px;top:62px;font-family:"Encode Sans",sans-serif;font-weight:400;font-size:20px;letter-spacing:3px;color:var(--navy);line-height:1;}
  .timeline{position:absolute;left:0;top:0;}
  .step-text{position:absolute;margin:0;font-weight:300;font-size:14.2px;line-height:19px;color:var(--navy);}
  .step-1{left:767px;top:212px;width:350px;}
  .step-2{left:117px;top:387px;width:345px;}
  .step-3{left:767px;top:552px;width:350px;}
  .step-4{left:117px;top:709px;width:345px;}
  .art{position:absolute;border-radius:8px;}
  .art-balance{left:189px;top:152px;width:250px;height:164px;background:linear-gradient(160deg,#cfe8f5,#a9d3ea);}
  .art-table{left:788px;top:340px;width:160px;height:144px;border-radius:50%;background:radial-gradient(circle,#e8f5fb,#a9d3ea);}
  .icons{position:absolute;left:0;top:0;}
</style>
</head>
<body>
<div class="canvas">
  <h1 class="title">STEPS OF MAKING A NEW DINING CONCEPT</h1>
  <div class="title-rule"></div>
  <div class="brand">GLEN MARBURY</div>

  <svg class="timeline" width="1200" height="849" viewBox="0 0 1200 849">
    <defs>
      <radialGradient id="disc" cx="40%" cy="35%" r="70%">
        <stop offset="0" stop-color="#eef8fd"/>
        <stop offset="1" stop-color="#b3d8ec"/>
      </radialGradient>
      <filter id="lift" x="-40%" y="-40%" width="180%" height="180%">
        <feDropShadow dx="0" dy="4" stdDeviation="4" flood-color="#5b8bb3" flood-opacity="0.45"/>
      </filter>
    </defs>
    <g class="guide-lines" fill="none" stroke="var(--rule)" stroke-width="1.2">
      <path d="M592 122 V196 M538 232 V278 M663 388 V442 M538 560 V606 M663 712 V770 M610 296 V370 M592 455 V540 M610 620 V700"/>
    </g>
    <g class="flow-line" fill="none" stroke="var(--navy)" stroke-width="3.2">
      <path d="M610 122 V196 A52 52 0 0 1 652 251 H692"/>
      <path d="M590 286 V364 A52 52 0 0 0 548 416 H505"/>
      <path d="M610 452 V530 A52 52 0 0 1 652 582 H692"/>
      <path d="M590 618 V692 A52 52 0 0 0 548 744 H505"/>
    </g>
    <g class="step-discs" font-family="Encode Sans, sans-serif" font-weight="400" font-size="19" fill="var(--navy)" text-anchor="middle">
      <circle cx="600" cy="251" r="37" fill="url(#disc)" filter="url(#lift)"/>
      <circle cx="600" cy="251" r="29" fill="none" stroke="#fff" stroke-opacity="0.6"/>
      <text x="600" y="258">1</text>
      <circle cx="600" cy="416" r="37" fill="url(#disc)" filter="url(#lift)"/>
      <circle cx="600" cy="416" r="29" fill="none" stroke="#fff" stroke-opacity="0.6"/>
      <text x="600" y="423">2</text>
      <circle cx="600" cy="582" r="37" fill="url(#disc)" filter="url(#lift)"/>
      <circle cx="600" cy="582" r="29" fill="none" stroke="#fff" stroke-opacity="0.6"/>
      <text x="600" y="589">3</text>
      <circle cx="600" cy="744" r="37" fill="url(#disc)" filter="url(#lift)"/>
      <circle cx="600" cy="744" r="29" fill="none" stroke="#fff" stroke-opacity="0.6"/>
      <text x="600" y="751">4</text>
    </g>
    <g class="arrow-buttons">
      <circle cx="708" cy="251" r="16" fill="var(--navy)"/>
      <path d="M705 244 L712 251 L705 258" fill="none" stroke="#fff" stroke-width="2.4"/>
      <circle cx="491" cy="416" r="16" fill="var(--navy)"/>
      <path d="M494 409 L487 416 L494 423" fill="none" stroke="#fff" stroke-width="2.4"/>
      <circle cx="708" cy="582" r="16" fill="var(--navy)"/>
      <path d="M705 575 L712 582 L705 589" fill="none" stroke="#fff" stroke-width="2.4"/>
      <circle cx="491" cy="744" r="16" fill="var(--navy)"/>
      <path d="M494 737 L487 744 L494 751" fill="none" stroke="#fff" stroke-width="2.4"/>
    </g>
  </svg>

  <div class="art art-balance" role="img" aria-label="Illustration of a balance scale weighing a dining table against a group of diners"></div>
  <div class="art art-table" role="img" aria-label="Illustration of a dining table setting, half sketched and half finished, between a fork and knife"></div>

  <svg class="icons" width="1200" height="849" viewBox="0 0 1200 849" fill="none" stroke="var(--navy)" stroke-width="2.4" stroke-linecap="round" stroke-linejoin="round">
    <g class="dividers" stroke="var(--rule)" stroke-width="1.2">
      <path d="M172 508 V566 M294 508 V566 M406 508 V566 M108 580 H480 M233 592 V648 M350 592 V648 M766 694 V772 M854 694 V772 M968 694 V772"/>
    </g>
    <g class="icon-menu">
      <rect x="94" y="508" width="44" height="56" fill="none"/>
      <rect x="80" y="514" width="40" height="54" fill="var(--navy)" stroke="none" rx="2"/>
      <path d="M124 518 H134 M124 526 H134 M124 534 H134 M124 542 H134 M124 550 H134" stroke-width="1.4"/>
      <path d="M89 541 A11 11 0 0 1 111 541 Z M87 543 H113" stroke="#fff" stroke-width="1.6"/>
      <text x="100" y="559" font-family="Encode Sans, sans-serif" font-size="7" fill="#fff" stroke="none" text-anchor="middle">MENU</text>
    </g>
    <g class="icon-analytics">
      <path d="M206 510 V562 H250"/>
      <path d="M216 556 V532 M224 556 V518 M232 556 V526 M240 540 V530"/>
      <circle cx="250" cy="550" r="11" fill="var(--bg)"/>
      <path d="M242 550 Q250 543 258 550 Q250 557 242 550 Z" stroke-width="1.6"/>
      <circle cx="250" cy="550" r="2" fill="var(--navy)"/>
    </g>
    <g class="icon-budget">
      <ellipse cx="360" cy="524" rx="14" ry="5"/>
      <path d="M346 524 V554 M374 524 V554 M346 532 Q360 539 374 532 M346 540 Q360 547 374 540 M346 548 Q360 555 374 548"/>
      <circle cx="342" cy="544" r="13" fill="var(--bg)"/>
      <text x="342" y="549" font-family="Encode Sans, sans-serif" font-size="14" font-weight="400" fill="var(--navy)" stroke="none" text-anchor="middle">$</text>
    </g>
    <g class="icon-operations">
      <circle cx="458" cy="538" r="14" stroke-width="6" stroke-dasharray="5 4"/>
      <circle cx="458" cy="538" r="9"/>
      <circle cx="488" cy="545" r="7" stroke-width="4" stroke-dasharray="3 3"/>
      <circle cx="488" cy="545" r="4" stroke-width="1.6"/>
    </g>
    <g class="icon-hierarchy">
      <rect x="160" y="598" width="22" height="14" fill="var(--navy)"/>
      <path d="M171 612 V620 M152 620 H190 M152 620 V627 M171 620 V627 M190 620 V627"/>
      <rect x="146" y="628" width="12" height="8" fill="var(--navy)"/>
      <rect x="165" y="628" width="12" height="8" fill="var(--navy)"/>
      <rect x="184" y="628" width="12" height="8" fill="var(--navy)"/>
    </g>
    <g class="icon-floorplan">
      <rect x="276" y="600" width="36" height="40"/>
      <path d="M276 614 H290 V626 M300 600 V612 H312 M290 640 V632 M300 626 H312"/>
    </g>
    <g class="icon-adjust">
      <path d="M380 604 H398 L402 596 L406 612 L410 604 H432"/>
      <path d="M380 620 H404 L408 612 L412 628 L416 620 H432"/>
      <path d="M380 636 H388 L392 628 L396 644 L400 636 H432"/>
    </g>
    <g class="icon-glass">
      <path d="M712 710 H748 L746 732 Q730 746 714 732 Z"/>
      <path d="M730 742 V752 M718 754 H742"/>
      <rect x="722" y="718" width="12" height="10" transform="rotate(-15 728 723)" stroke-width="1.6"/>
    </g>
    <g class="icon-bowl">
      <path d="M786 726 H834 V738 Q834 754 818 754 H802 Q786 754 786 738 Z"/>
      <path d="M800 726 Q796 712 806 704 M812 726 Q812 712 820 708 M822 726 Q826 714 830 712"/>
    </g>
    <g class="icon-table">
      <path d="M892 728 H936 M914 728 V752 M906 752 H922"/>
      <path d="M876 712 L880 732 L874 754 M880 732 H892 L896 754 M876 712 L890 706 L892 728"/>
      <path d="M952 712 L948 732 L954 754 M948 732 H936 L932 754 M952 712 L938 706 L936 728"/>
    </g>
    <g class="icon-place-setting">
      <circle cx="1026" cy="730" r="26"/>
      <path d="M990 704 V722 M986 704 V716 Q986 722 990 722 Q994 722 994 716 V704 M990 722 V756"/>
      <path d="M1064 704 Q1058 716 1060 730 L1062 732 V756"/>
    </g>
  </svg>

  <p class="step-text step-1">We analyse your current offering: menus, dining environment, how they are presented and sold, and weigh them up against your target demographic, and their expectations of cuisine and pricing.</p>
  <p class="step-text step-2">Using our unique modelling software, we iteratively refine your outline concepts to create the vision of the dining experience that is the best that it can be.</p>
  <p class="step-text step-3">We create executable Blueprints of everything from recipes to beverages, staffing hierarchies to floor plans, sales and marketing plans to budgets.</p>
  <p class="step-text step-4">We guide you through the execution, mentoring your heads of department to ensure the realisation of your concept matches the original vision.</p>
</div>
</body>
</html>
```